Design a business card & stationary for a mortgage company

We are looking for a good looking business card design for our mortgage company that includes our logo. We received a free design as part of our logo project but we don't love it. The company is called "Pinecrest Mortgage Company" so we like waves and lighthouses. The logo should be included. We have a version in both vertical and horizontal that we have provided.

Industry/Entity Type

Finance

Contact Information for Business Card

This should include our new logo file

Requirements
Must have
• 3. The details you'd like on the card - name, title, phone, email, website, address, social media handles etc.
1. Marcus Hale
Vice President
732-419-6253
Fax 888-304-2918
mhale@pinecrestmortgage.example
NMLS 47162 - Company NMLS 61290
18 Larkin Ave
Harbor Point, NJ 08614

```html
<!DOCTYPE html>
<html lang="en">
<head>
<meta charset="utf-8">
<title>Pinecrest Mortgage Company – Business Card</title>
<link rel="stylesheet" href="https://fonts.googleapis.com/css2?family=Open+Sans:ital,wght@0,300;0,400;0,700;1,400;1,700&display=swap">
<style>
  :root {
    --navy: #175a8c;
    --bright-blue: #1a8ccf;
    --cream: #f3f0e3;
    --cream-ink: #f1ecd8;
    --slate: #555a60;
    --backdrop: #e4e2dc;
  }
  * { box-sizing: border-box; margin: 0; padding: 0; }
  html, body { width: 1200px; height: 787px; overflow: hidden; }
  body {
    background: var(--backdrop);
    font-family: "Open Sans", Arial, sans-serif;
    display: flex;
    align-items: center;
    justify-content: center;
    gap: 60px;
  }
  .card {
    width: 525px;
    height: 300px;
    position: relative;
    box-shadow: 0 6px 18px rgba(0,0,0,.18);
    overflow: hidden;
  }
  /* Front */
  .card-front { background: var(--cream); }
  .edge-band-left {
    position: absolute; left: 0; top: 0; bottom: 0; width: 16px;
    background: linear-gradient(to bottom, var(--bright-blue) 0 62%, var(--navy) 62% 100%);
  }
  .edge-band-right {
    position: absolute; right: 0; top: 0; bottom: 0; width: 16px;
    background: linear-gradient(to bottom, var(--bright-blue) 0 55%, var(--navy) 55% 100%);
  }
  .brand-front {
    position: absolute; left: 190px; top: 42px; width: 300px;
    color: var(--navy);
    display: flex; flex-direction: column; align-items: flex-end;
  }
  .brand-name {
    display: flex; align-items: center; gap: 10px;
    font-weight: 700; font-size: 30px; letter-spacing: 1px; line-height: 1;
  }
  .brand-dot { width: 14px; height: 14px; border-radius: 50%; background: currentColor; }
  .brand-sub {
    font-weight: 700; font-size: 12px; letter-spacing: 4px; margin-top: 6px;
  }
  .brand-tagline {
    font-weight: 700; font-size: 8px; letter-spacing: 2px; margin-top: 4px;
  }
  .person { position: absolute; left: 56px; top: 140px; }
  .person-name { font-size: 34px; color: var(--slate); line-height: 1.05; letter-spacing: -0.5px; }
  .person-name .first { font-weight: 700; }
  .person-name .last { font-weight: 300; }
  .person-title {
    color: var(--bright-blue); font-weight: 700; font-style: italic;
    font-size: 14px; letter-spacing: .5px; margin-top: 2px;
  }
  .contact-list {
    position: absolute; left: 44px; top: 218px;
    list-style: none; color: var(--slate); font-size: 13px;
    display: grid; grid-template-columns: auto auto; column-gap: 34px; row-gap: 8px;
  }
  .contact-list li { display: flex; align-items: center; gap: 8px; }
  .contact-list .email { grid-column: 1 / span 2; }
  .contact-list svg { width: 16px; height: 16px; fill: var(--bright-blue); flex: none; }
  /* Back */
  .card-back { background: var(--navy); color: var(--cream-ink); }
  .brand-back {
    position: absolute; left: 0; right: 0; top: 78px;
    display: flex; flex-direction: column; align-items: center;
  }
  .brand-back .brand-name { font-size: 32px; }
  .company-details {
    position: absolute; left: 0; right: 0; top: 190px;
    text-align: center; font-size: 13px; line-height: 1.7; font-weight: 400;
  }
  .company-details .sep { margin: 0 10px; }
</style>
</head>
<body>
  <section class="card card-front" aria-label="Business card front">
    <div class="edge-band-left"></div>
    <div class="edge-band-right"></div>
    <div class="brand-front">
      <div class="brand-name"><span class="brand-dot"></span>PINECREST</div>
      <div class="brand-sub">MORTGAGE COMPANY</div>
      <div class="brand-tagline">ROOTED IN TRUST</div>
    </div>
    <div class="person">
      <div class="person-name"><span class="first">Marcus</span><span class="last">Hale</span></div>
      <div class="person-title">VICE PRESIDENT</div>
    </div>
    <ul class="contact-list">
      <li class="phone">
        <svg viewBox="0 0 24 24" aria-hidden="true"><path d="M6.6 10.8a15 15 0 0 0 6.6 6.6l2.2-2.2a1 1 0 0 1 1-.25 11.4 11.4 0 0 0 3.6.57 1 1 0 0 1 1 1V20a1 1 0 0 1-1 1A17 17 0 0 1 3 4a1 1 0 0 1 1-1h3.5a1 1 0 0 1 1 1c0 1.25.2 2.45.57 3.57a1 1 0 0 1-.25 1z"/></svg>
        732-419-6253
      </li>
      <li class="fax">
        <svg viewBox="0 0 24 24" aria-hidden="true"><path d="M7 3h8l3 3v4H7zM3 10h18v10H3zm3 3v2h3v-2zm5 0v2h3v-2z"/></svg>
        888-304-2918
      </li>
      <li class="email">
        <svg viewBox="0 0 24 24" aria-hidden="true"><path d="M2 5h20v14H2zm2 2v.5l8 5 8-5V7l-8 5z"/></svg>
        mhale@pinecrestmortgage.example
      </li>
    </ul>
  </section>

  <section class="card card-back" aria-label="Business card back">
    <div class="brand-back">
      <div class="brand-name"><span class="brand-dot"></span>PINECREST</div>
      <div class="brand-sub">MORTGAGE COMPANY</div>
      <div class="brand-tagline">ROOTED IN TRUST</div>
    </div>
    <div class="company-details">
      <div>NMLS 47162 - Company NMLS 61290</div>
      <div>18 Larkin Ave<span class="sep">/</span>Harbor Point, NJ 08614</div>
    </div>
  </section>
</body>
</html>
```